Commercial Cleaning Company Website Design

We are working with Harbor Sweep Team. They are a commercial cleaning company that needs a new website design.

Some sites to use for inspiration:

https://www.plenvask.com
https://glint-panecleaning.com
https://tidyhelpers.net
https://calmnesthouse.com
https://www.thecleaningbureauxyz.com
https://www.dottiebroom.com

Thank you for taking the time to consider designing a website for us. We are web developers based in Stockton and Los Angeles, CA, USA. Most of our projects go through the same process. Understanding this process may help you win a project with us. We custom-code all of our websites in-house. We don’t have any requirements as to what tools you use for your design, but we prefer Figma files. For any design that we label as four-stars, we send it to the client for review. The client picks the final design they want us to use. Once we complete this process, we will continue to show additional clients all the four-star sites and purchase them later. Your designs will have multiple chances to sell. For better chances of success, we ask that you follow these guidelines.

IMAGES:
If you use any images or icons in the design, we ask that you have a link to the asset so we can purchase the image/icon. Most of the designs we submit do not have the customer’s images on them unless they have some great images. Be creative; show us the feeling you are trying to portray with your image choices. Use any royalty-free site you choose. We subscribe to Adobe and mainly use their images, but we can purchase images outside of Adobe.

PLEASE NOTE: we will not submit designs to clients with watermarks on the images.

FONTS:
We ask that you identify the fonts used in the design. This can be done in a message if you want. We typically use Google Fonts and Adobe Fonts.

CONTENT:
We're always open to different content and ideas. We often submit designs with stock images so the client can see our vision. We typically take pictures after the website launch to use their images with our vision. Lorem Ipsum is fine for paragraphs, but we ask that you write the headers in correct English. We want to be able to show the vision and identify the sections of the website.

INSPIRATION:
We typically add a couple of links in the brief of websites we like to help you get started in your design.

REVISIONS:
We do not often ask for revisions of the designs unless we see something in the design that may not appeal to the client. If there are slight changes that we want to make, we do that in the development process.

FEEDBACK:
We rarely give feedback on designs during the design process. We are working on many website projects and do not have the time to provide feedback. We usually respond if your request is well thought out and asks specific questions, but a note asking “feedback, please” usually goes unanswered.

```html
<!DOCTYPE html>
<html lang="en">
<head>
<meta charset="utf-8">
<title>Harbor Sweep Team — Commercial Cleaning</title>
<link href="https://fonts.googleapis.com/css2?family=Plus+Jakarta+Sans:ital,wght@0,400;0,500;0,600;0,700;1,400&display=swap" rel="stylesheet">
<style>
:root{
  --blue:#1a4fc4;
  --blue-deep:#173f9e;
  --blue-dark:#12306f;
  --yellow:#f6a60f;
  --ink:#151515;
  --text:#2b2b2b;
  --white:#ffffff;
  --line:#e7e9ef;
}
*{margin:0;padding:0;box-sizing:border-box}
html,body{width:1200px;height:3756px;overflow:hidden}
body{position:relative;font-family:"Plus Jakarta Sans",sans-serif;color:var(--ink);background:var(--white)}
.abs{position:absolute}
.center{left:0;width:1200px;text-align:center}
.btn{position:absolute;display:flex;align-items:center;justify-content:center;font-size:16px;font-weight:500;border-radius:3px}
.btn::after{content:"";position:absolute;bottom:3px;left:50%;width:50px;margin-left:-25px;height:2px;background:currentColor}
.btn-outline-blue{border:1.5px solid var(--blue);color:var(--blue);background:var(--white)}
.btn-outline-blue::after{background:var(--blue)}
.btn-outline-yellow{border:1.5px solid var(--yellow);color:var(--yellow)}
.btn-solid{background:var(--blue);color:var(--yellow);border:1.5px solid var(--yellow)}
.btn-solid::after{background:var(--yellow)}
.eyebrow{color:var(--yellow);font-weight:500;font-size:26px}
.heading{font-weight:500;font-size:40px;letter-spacing:-.3px}

/* header */
.site-header{left:0;top:0;width:1200px;height:125px;background:var(--white)}
.brand{display:flex;align-items:center;gap:10px}
.brand-dot{width:18px;height:18px;border-radius:50%;background:var(--yellow)}
.brand-name{font-weight:600;color:var(--blue);letter-spacing:3px;font-size:15px}
.nav a{position:absolute;top:51px;font-size:16px;color:var(--ink);text-decoration:none}
.nav a.active{color:var(--blue);font-style:italic;font-weight:600;text-decoration:underline;font-size:18px;top:49px}

/* hero */
.hero{left:0;top:125px;width:1200px;height:556px;background:linear-gradient(100deg,#5b7196 0%,#3e5478 35%,#2e4466 65%,#4b5f7f 100%)}
.hero-overlay{left:0;top:0;width:1200px;height:556px;background:rgba(22,42,90,.35)}

/* services */
.feature-card{left:115px;top:988px;width:411px;height:572px;background:var(--blue);border:1.5px solid var(--yellow);border-radius:4px;box-shadow:0 10px 24px rgba(0,0,0,.18);overflow:hidden}
.feature-photo{left:0;top:0;width:411px;height:308px;background:linear-gradient(180deg,#e9eef3,#c9d2dc 60%,#8a9bb0)}
.service-item{width:248px;text-align:center}
.service-item .title{color:var(--blue);font-weight:500;font-size:26px;line-height:30px}
.service-item.active{background:var(--white);box-shadow:0 6px 24px rgba(0,0,0,.09);border-radius:6px}
.service-item.active .title{color:var(--yellow)}

/* projects */
.projects{left:0;top:1669px;width:1200px;height:766px;background:linear-gradient(180deg,#1b4fc3 0%,#1a46ad 55%,#143781 100%)}
.thumb{top:2111px;height:207px;border-radius:2px}
.result-card{left:678px;top:1750px;width:411px;height:570px;background:var(--blue);border:1.5px solid #6f8fd8;border-radius:4px;overflow:hidden}

/* about */
.bullets li{position:relative;list-style:none;font-size:16px;line-height:26px;color:var(--text)}
.bullets li::before{content:"";position:absolute;left:-28px;top:10px;width:6px;height:6px;border-radius:50%;background:var(--blue)}

/* cta */
.cta{left:0;top:3174px;width:1200px;height:321px;background:linear-gradient(180deg,#6d86ad 0%,#4f6893 50%,#5a7097 100%)}

/* footer */
.footer-links a{position:absolute;top:3628px;font-size:16px;color:var(--ink);text-decoration:none}
.footer-links a.active{color:var(--blue);font-style:italic;font-weight:600;text-decoration:underline;font-size:18px;top:3626px}
.social{position:absolute;top:3684px;width:24px;height:24px;border-radius:50%;background:var(--blue)}
</style>
</head>
<body>

<!-- Header -->
<header class="abs site-header">
  <div class="abs brand" style="left:112px;top:50px">
    <span class="brand-dot"></span><span class="brand-name">HARBOR SWEEP TEAM</span>
  </div>
  <nav class="nav">
    <a class="active" style="left:357px">Home</a>
    <a style="left:445px">About Us</a>
    <a style="left:548px">Services</a>
    <a style="left:647px">Projects</a>
    <a style="left:745px">Contact</a>
  </nav>
  <svg class="abs" style="left:860px;top:54px" width="16" height="16" viewBox="0 0 16 16"><circle cx="6.5" cy="6.5" r="4.5" fill="none" stroke="#1a4fc4" stroke-width="2"/><line x1="10" y1="10" x2="14" y2="14" stroke="#1a4fc4" stroke-width="2.2"/></svg>
  <div class="btn btn-solid" style="left:937px;top:39px;width:151px;height:46px;box-shadow:0 3px 8px rgba(0,0,0,.2)">Get Started</div>
</header>

<!-- Hero -->
<section class="abs hero" role="img" aria-label="Two cleaners at work in a bright glass-walled office, one wiping a desk and one vacuuming">
  <div class="abs hero-overlay"></div>
</section>
<div class="abs center" style="top:292px;color:var(--yellow);font-size:40px;font-weight:600;letter-spacing:-.5px">HARBOR SWEEP TEAM</div>
<h1 class="abs center" style="top:344px;color:var(--white);font-size:50px;font-weight:600;letter-spacing:-.5px">Spotless Spaces | Professional Results</h1>
<p class="abs center" style="top:420px;color:var(--white);font-size:17px;line-height:26px">Harbor Sweep Team delivers top-tier commercial cleaning for offices, buildings, and facilities<br>Fast, reliable, and tailored to your business needs.</p>
<div class="btn btn-outline-yellow" style="left:525px;top:510px;width:150px;height:46px">Learn More</div>

<!-- Services -->
<div class="abs center eyebrow" style="top:764px">Services We Offer</div>
<h2 class="abs center heading" style="top:808px">Our Commercial Cleaning Solutions</h2>
<p class="abs center" style="top:876px;font-size:16px;line-height:27px;color:var(--text)">Harbor Sweep Team provides a full range of professional commercial cleaning services designed<br>to keep your workplace spotless, safe, and welcoming.</p>

<article class="abs feature-card">
  <div class="abs feature-photo" role="img" aria-label="Cleaner in blue uniform wiping a desk in an open-plan office"></div>
  <div class="abs" style="left:0;top:334px;width:411px;text-align:center;color:var(--yellow);font-size:26px;font-weight:500">General Office Cleaning</div>
  <p class="abs" style="left:40px;top:386px;width:331px;text-align:center;color:var(--white);font-size:16px;line-height:26px">Daily or scheduled cleaning including dusting, vacuuming, trash removal, and surface sanitation for all office areas.</p>
  <div class="btn btn-outline-yellow" style="left:131px;top:487px;width:151px;height:46px">Contact Us</div>
</article>

<div class="abs service-item active" style="left:583px;top:988px;height:301px"></div>
<svg class="abs" style="left:678px;top:1030px" width="60" height="56" viewBox="0 0 60 56" fill="none" stroke="#f6a60f" stroke-width="2.2"><rect x="2" y="2" width="22" height="52"/><rect x="24" y="16" width="34" height="38"/><line x1="2" y1="14" x2="24" y2="14"/><line x1="2" y1="28" x2="24" y2="28"/><line x1="2" y1="42" x2="24" y2="42"/><line x1="36" y1="30" x2="46" y2="30"/><line x1="36" y1="40" x2="46" y2="40"/></svg>
<div class="abs service-item" style="left:583px;top:1106px"><div class="title" style="color:var(--yellow)">General Office<br>Cleaning</div></div>
<div class="btn btn-solid" style="left:632px;top:1197px;width:151px;height:46px;color:var(--yellow)">Learn More</div>

<svg class="abs" style="left:972px;top:1026px" width="64" height="66" viewBox="0 0 64 66" fill="none" stroke="#1a4fc4" stroke-width="2.2"><path d="M26 62 V14 a10 10 0 0 1 20 0 L62 62"/><circle cx="10" cy="56" r="6"/><path d="M16 52 L26 46 M4 42 H26"/></svg>
<div class="abs service-item" style="left:879px;top:1106px"><div class="title">Floor &amp; Carpet<br>Cleaning</div></div>
<div class="btn btn-outline-blue" style="left:928px;top:1197px;width:151px;height:46px">Learn More</div>

<svg class="abs" style="left:686px;top:1322px" width="58" height="64" viewBox="0 0 58 64" fill="none" stroke="#1a4fc4" stroke-width="2.2"><rect x="6" y="20" width="28" height="42" rx="6"/><path d="M14 20 V8 H28 V20 M28 10 H38"/><line x1="20" y1="32" x2="20" y2="50"/><line x1="11" y1="41" x2="29" y2="41"/><path d="M48 24 q6 9 0 14 q-6-5 0-14z" fill="#1a4fc4"/></svg>
<div class="abs service-item" style="left:583px;top:1401px"><div class="title">Sanitization &amp;<br>Disinfection</div></div>
<div class="btn btn-outline-blue" style="left:632px;top:1491px;width:151px;height:46px">Learn More</div>

<svg class="abs" style="left:964px;top:1326px" width="80" height="56" viewBox="0 0 80 56" fill="none" stroke="#1a4fc4" stroke-width="2.2"><rect x="2" y="20" width="24" height="26"/><rect x="26" y="4" width="26" height="42"/><path d="M52 14 H62 L72 46 H52"/><circle cx="14" cy="48" r="6" fill="#fff"/><circle cx="46" cy="48" r="6" fill="#fff"/></svg>
<div class="abs service-item" style="left:879px;top:1401px"><div class="title">Construction<br>Clean-Up</div></div>
<div class="btn btn-outline-blue" style="left:928px;top:1491px;width:151px;height:46px">Learn More</div>

<!-- Projects -->
<section class="abs projects"></section>
<div class="abs eyebrow" style="left:112px;top:1767px">Our Featured Projects</div>
<div class="abs" style="left:543px;top:1770px;width:28px;height:28px;border-radius:50%;background:#6b7fa8"></div>
<svg class="abs" style="left:550px;top:1777px" width="14" height="14" viewBox="0 0 14 14"><path d="M9 3 L5 7 L9 11" fill="none" stroke="#1a3f8f" stroke-width="2"/></svg>
<div class="abs" style="left:588px;top:1770px;width:28px;height:28px;border-radius:50%;background:var(--yellow)"></div>
<svg class="abs" style="left:595px;top:1777px" width="14" height="14" viewBox="0 0 14 14"><path d="M5 3 L9 7 L5 11" fill="none" stroke="#12306f" stroke-width="2"/></svg>
<h2 class="abs heading" style="left:110px;top:1812px;color:var(--white);line-height:44px">Crown Post Offices,<br>Deptford</h2>
<p class="abs" style="left:112px;top:1920px;width:500px;color:var(--white);font-size:16px;line-height:26px">Completed a high-specification cleaning service across the entire delivery office, focusing on flooring, toilets, and high-level areas, ensuring a spotless and hygienic environment.</p>
<div class="abs eyebrow" style="left:112px;top:2042px">More of Our Projects</div>
<div class="btn btn-outline-yellow" style="left:468px;top:2038px;width:150px;height:46px">View All</div>
<div class="abs thumb" style="left:111px;width:163px;background:linear-gradient(180deg,#eef1f4,#c5ccd4);border:1.5px solid var(--yellow);box-shadow:0 10px 20px rgba(0,0,0,.3)" role="img" aria-label="Clean open-plan office with white desks"></div>
<div class="abs thumb" style="left:296px;width:149px;background:linear-gradient(180deg,#b9c1c9,#8f99a4)" role="img" aria-label="Floor scrubbing machine polishing a tiled floor"></div>
<div class="abs thumb" style="left:464px;width:150px;background:linear-gradient(180deg,#a9c4dc,#5f7f6a)" role="img" aria-label="Glass office building behind green trees"></div>

<article class="abs result-card">
  <div class="abs" style="left:0;top:0;width:411px;height:300px;background:linear-gradient(180deg,#f2f4f6,#d3d9df 70%,#b5bec7)" role="img" aria-label="Bright office interior with desks, chairs and plants"></div>
  <div class="abs" style="left:0;top:338px;width:411px;text-align:center;color:var(--yellow);font-size:26px;font-weight:500">Results of Our Work</div>
  <p class="abs" style="left:30px;top:393px;width:351px;text-align:center;color:var(--white);font-size:16px;line-height:26px;font-style:italic">“Impeccable cleanliness and efficient service aligned with client expectations.”</p>
  <div class="abs" style="left:0;top:479px;width:411px;text-align:center;color:var(--white);font-size:16px">Daniel Okafor, Founder/CEO</div>
  <div class="abs" style="left:0;top:510px;width:411px;text-align:center;color:var(--yellow);font-size:14px;font-weight:500">Crown Post Services, Deptford</div>
</article>

<!-- About -->
<div class="abs" style="left:112px;top:2537px;width:410px;height:539px;background:linear-gradient(180deg,#6b7684,#3c4654 55%,#8a929c);border:1.5px solid var(--yellow);border-radius:3px;box-shadow:0 10px 30px rgba(0,0,0,.15)" role="img" aria-label="Two window cleaners on a lift platform cleaning a glass facade"></div>
<div class="abs eyebrow" style="left:605px;top:2557px">About Us</div>
<h2 class="abs heading" style="left:604px;top:2610px">Who We Are</h2>
<ul class="abs bullets" style="left:634px;top:2693px;width:470px">
  <li>Harbor Sweep Team is your trusted partner for professional commercial cleaning.</li>
  <li style="margin-top:25px">As a locally owned and operated company, we take pride in delivering reliable, high-quality cleaning solutions tailored to the unique needs of businesses across our community.</li>
  <li style="margin-top:25px">Backed by years of experience and a dedicated team of certified cleaning professionals, we believe a spotless workplace is essential for productivity, employee health, and customer confidence.</li>
</ul>
<div class="btn btn-outline-blue" style="left:634px;top:3018px;width:151px;height:46px">Learn More</div>

<!-- CTA -->
<section class="abs cta" role="img" aria-label="Rope-access cleaner on a tall glass tower seen from below"></section>
<div class="abs center" style="top:3241px;color:var(--yellow);font-size:40px;font-weight:600;letter-spacing:-.4px">Ready for a Cleaner, Healthier Workspace?</div>
<div class="abs center" style="top:3292px;color:var(--white);font-size:40px;font-weight:500">Let’s talk.</div>
<div class="btn btn-solid" style="left:525px;top:3375px;width:150px;height:46px">Contact Us</div>

<!-- Footer -->
<footer>
  <div class="abs brand" style="left:117px;top:3590px;gap:14px">
    <span class="brand-dot" style="width:28px;height:28px"></span>
    <span class="brand-name" style="font-size:28px;letter-spacing:6px">HARBOR SWEEP TEAM</span>
  </div>
  <div class="abs" style="left:113px;top:3686px;font-size:16px;color:var(--blue)">©2025 Harbor Sweep Team. All Rights Reserved.</div>
  <div class="abs eyebrow" style="left:642px;top:3565px">Quick Links</div>
  <nav class="footer-links">
    <a class="active" style="left:642px">Home</a>
    <a style="left:729px">About Us</a>
    <a style="left:833px">Services</a>
    <a style="left:932px">Projects</a>
    <a style="left:1030px">Contact</a>
  </nav>
  <div class="abs eyebrow" style="left:643px;top:3680px">Follow us</div>
  <span class="social" style="left:800px"></span>
  <span class="social" style="left:842px"></span>
  <span class="social" style="left:885px"></span>
  <span class="social" style="left:926px"></span>
</footer>

</body>
</html>
```